Carpet cleaning company wants business card

Need an exciting new fresh design for business cards for my carpet cleaning /pest control business
www.tidewellhomecare.com.au
Can design include a lined section for quoting or information? Thanks !

```html
<!DOCTYPE html>
<html lang="en">
<head>
<meta charset="utf-8">
<title>Tidewell Home Care – Business Card</title>
<link href="https://fonts.googleapis.com/css2?family=Montserrat:wght@500;800&family=Archivo+Narrow:wght@600&display=swap" rel="stylesheet">
<style>
  :root {
    --backdrop: #808080;
    --card: #ffffff;
    --brand-blue: #0a56a6;
    --brand-red: #e63b36;
    --van-light: #f1f4f8;
    --van-mid: #c9d2de;
    --rule: #9fb6d3;
    --shadow: rgba(0,0,0,0.28);
  }
  html, body {
    margin: 0;
    width: 1200px;
    height: 1000px;
    overflow: hidden;
    background: var(--backdrop);
  }
  .canvas { position: relative; width: 1200px; height: 1000px; }
  .card {
    position: absolute;
    background: var(--card);
    border-radius: 22px;
    box-shadow: 0 10px 24px var(--shadow);
    overflow: hidden;
  }
  .card--front { left: 250px; top: 125px; width: 610px; height: 410px; }
  .card--back  { left: 400px; top: 550px; width: 610px; height: 370px; }

  .front-panel { position: absolute; inset: 0; }

  .brand-vertical {
    position: absolute;
    left: 20px;
    top: 388px;
    transform-origin: left top;
    transform: rotate(-90deg);
    display: flex;
    align-items: center;
    gap: 12px;
    white-space: nowrap;
  }
  .brand-name {
    font-family: "Montserrat", sans-serif;
    font-weight: 800;
    color: var(--brand-blue);
    line-height: 1;
  }
  .brand-vertical .brand-name { font-size: 64px; letter-spacing: -1.5px; }
  .brand-mark {
    flex: none;
    width: 20px;
    height: 20px;
    background: var(--brand-red);
    border-radius: 50%;
  }

  .contact {
    position: absolute;
    left: 165px;
    top: 80px;
    display: flex;
    align-items: flex-start;
    gap: 16px;
    color: #fff;
    font-family: "Montserrat", sans-serif;
    font-weight: 500;
    font-size: 15px;
    line-height: 18px;
  }
  .contact-lines { margin: 0; padding: 0; list-style: none; }

  .scene-art {
    position: absolute;
    left: 195px;
    top: 178px;
    width: 395px;
    height: 232px;
    border-radius: 40px 60px 0 0;
    background: linear-gradient(180deg, var(--van-light) 0%, var(--van-mid) 100%);
  }

  .back-content {
    position: absolute;
    inset: 0;
    padding-top: 100px;
    display: flex;
    flex-direction: column;
    align-items: center;
    gap: 12px;
  }
  .back-brand { display: flex; align-items: center; gap: 10px; }
  .back-brand .brand-name { font-size: 32px; letter-spacing: -0.5px; }
  .back-brand .brand-mark { width: 14px; height: 14px; }
  .service-list {
    margin: 0;
    text-align: center;
    font-family: "Archivo Narrow", sans-serif;
    font-weight: 600;
    font-size: 9px;
    line-height: 11px;
    letter-spacing: 0.2px;
    text-transform: uppercase;
    color: var(--brand-blue);
  }
  .quote-lines {
    margin-top: 18px;
    width: 440px;
    display: flex;
    flex-direction: column;
    gap: 22px;
  }
  .quote-line { height: 0; border-bottom: 1px solid var(--rule); }
</style>
</head>
<body>
<main class="canvas">

  <section class="card card--front" aria-label="Business card front">
    <svg class="front-panel" width="610" height="410" viewBox="0 0 610 410" aria-hidden="true">
      <rect class="brand-bar" x="90" y="65" width="12" height="320" fill="var(--brand-blue)"/>
      <path class="blue-panel" d="M150 88 Q130 92 128 112 L195 410 H610 V40 Z" fill="var(--brand-blue)"/>
    </svg>

    <div class="brand-vertical">
      <span class="brand-mark"></span>
      <span class="brand-name">Tidewell</span>
    </div>

    <div class="contact">
      <svg class="contact-icon" width="36" height="56" viewBox="0 0 36 56" aria-hidden="true" fill="none" stroke="#fff" stroke-width="1.6">
        <rect x="2" y="2" width="26" height="52" rx="2"/>
        <path d="M28 22 L34 26 L28 30"/>
        <path d="M9 10 q2 6 8 9 l2-2 2 2 -2 3 q-8-3-11-12 z"/>
        <rect x="10" y="26" width="9" height="12" rx="1.5"/>
        <rect x="8" y="42" width="13" height="9"/>
        <path d="M8 42 l6.5 5 6.5-5"/>
      </svg>
      <ul class="contact-lines">
        <li>07 5550 1200</li>
        <li>0400 555 017</li>
        <li>admin@tidewellhomecare.com.au</li>
      </ul>
    </div>

    <div class="scene-art" role="img" aria-label="Illustration of two cleaning technicians in navy uniforms standing in front of a white company van"></div>
  </section>

  <section class="card card--back" aria-label="Business card back">
    <div class="back-content">
      <div class="back-brand">
        <span class="brand-mark"></span>
        <span class="brand-name">Tidewell Home Care</span>
      </div>
      <p class="service-list">
        Residential carpet cleaning | Commercial carpet cleaning | Vacate carpet cleaning and pest control<br>
        Pest control | Furniture and upholstery cleaning | Tile and grout cleaning<br>
        Water extraction service | Mats and rug cleaning
      </p>
      <div class="quote-lines" aria-label="Lined space for quotes and notes">
        <div class="quote-line"></div>
        <div class="quote-line"></div>
        <div class="quote-line"></div>
        <div class="quote-line"></div>
      </div>
    </div>
  </section>

</main>
</body>
</html>
```